Takeout menu

I need a takeout menu for Dino Kettle in Westerly RI. It needs just the location, phone number, items and descriptions from my square site- no pricing listed. No hours listed as I am seasonal and they change during the year. Must say "please inform us of any food allergies prior to ordering" somewhere on it, per order of health dept. I will most likely be printing in b/w.

```html
<!DOCTYPE html>
<html lang="en">
<head>
<meta charset="utf-8">
<title>Dino Kettle Takeout Menu</title>
<link href="https://fonts.googleapis.com/css2?family=Alfa+Slab+One&family=Chewy&family=Dela+Gothic+One&family=Lexend:wght@300;400&family=Fredoka:wght@600&display=swap" rel="stylesheet">
<style>
:root{
  --stage:#a0a0a0;
  --paper:#fbf8ef;
  --sand:#e7e2c5;
  --red:#e2001a;
  --brown:#6b5628;
  --ink:#5e4a24;
  --cheese:#f6e79a;
  --crust:#f4b23a;
  --basil:#6f9a3a;
  --white:#ffffff;
}
*{margin:0;padding:0;box-sizing:border-box}
html,body{width:839px;height:1200px;overflow:hidden;background:var(--stage)}
.menu{
  position:absolute;left:111.4px;top:72.2px;width:1178px;height:2020px;
  transform:scale(0.5232);transform-origin:0 0;
  background:var(--paper);overflow:hidden;
  font-family:"Lexend",sans-serif;color:var(--ink);
}
.art{position:absolute}
.masthead-tag{position:absolute;left:339px;top:52px;font-family:"Fredoka",sans-serif;font-weight:600;font-size:46px;color:var(--brown);z-index:2}
.masthead-title{position:absolute;left:74px;top:40px;font-family:"Chewy",cursive;font-size:220px;line-height:1;color:var(--red);letter-spacing:-4px}
.masthead-sub{position:absolute;left:405px;top:200px;font-family:"Chewy",cursive;font-size:120px;line-height:1;color:var(--brown)}
.rule{position:absolute;height:0;border-top:2px solid var(--red)}
.dash{position:absolute;border-top:2px dashed #9a8d6a;height:0}
.vdash{position:absolute;border-left:2px dashed #9a8d6a;width:0}
.section-title{position:absolute;font-family:"Alfa Slab One",serif;font-size:34px;color:var(--red);letter-spacing:2px;line-height:1;white-space:nowrap}
.section-note{position:absolute;font-size:10px;color:var(--ink);line-height:13px}
.item{position:absolute;width:325px}
.item h3{font-family:"Dela Gothic One",sans-serif;font-weight:400;font-size:18px;color:var(--brown);letter-spacing:0;line-height:24px;text-transform:uppercase;white-space:nowrap}
.item p{margin-top:8px;font-size:14px;line-height:16.8px;font-weight:300;color:var(--ink)}
.order-head{position:absolute;left:89px;top:1730px;font-family:"Dela Gothic One",sans-serif;font-size:38px;color:var(--red);letter-spacing:1px;line-height:1;white-space:nowrap}
.order-phone{position:absolute;left:180px;top:1784px;font-family:"Dela Gothic One",sans-serif;font-size:57px;color:var(--brown);line-height:1;white-space:nowrap}
.order-address{position:absolute;left:146px;top:1868px;font-family:"Dela Gothic One",sans-serif;font-size:21px;color:var(--brown);line-height:1;letter-spacing:.5px;white-space:nowrap}
.icon{position:absolute}
.allergy-band{position:absolute;left:0;top:1920px;width:1178px;height:100px}
.allergy-note{position:absolute;left:0;top:1962px;width:1178px;text-align:center;color:var(--white);font-size:25px;font-weight:400}
</style>
</head>
<body>
<main class="menu">
  <svg class="art" width="1178" height="540" viewBox="0 0 1178 540" aria-hidden="true">
    <path d="M0 0H945C930 40 920 90 880 150C840 230 780 260 760 330C745 380 690 390 600 385C520 380 460 370 380 360C250 340 120 300 0 270Z" fill="var(--sand)"/>
  </svg>
  <svg class="art" style="left:0;top:250px" width="400" height="280" viewBox="0 0 400 280" role="img" aria-label="Illustrated pepperoni pizza slice">
    <path d="M0 0L390 50L0 272Z" fill="var(--cheese)"/>
  </svg>
  <svg class="art" style="left:670px;top:55px" width="450" height="315" viewBox="0 0 450 315" role="img" aria-label="Illustrated pizza slice flying with melting cheese and the shop name">
    <path d="M440 5L240 300L100 250L20 310L60 200L150 90Z" fill="var(--crust)"/>
  </svg>
  <svg class="art" style="left:1040px;top:225px" width="138" height="250" viewBox="0 0 138 250" role="img" aria-label="Illustrated round pepperoni decoration">
    <path d="M138 0V245C60 240 0 190 5 120C10 50 70 5 138 0Z" fill="var(--red)"/>
  </svg>
  <svg class="art" style="left:915px;top:1185px" width="263" height="200" viewBox="0 0 263 200" role="img" aria-label="Illustrated pepperoni pizza slice">
    <path d="M0 55L263 5V195Z" fill="var(--cheese)"/>
  </svg>
  <svg class="art" style="left:0;top:1415px" width="70" height="125" viewBox="0 0 70 125" role="img" aria-label="Illustrated round pepperoni decoration">
    <path d="M0 0C40 5 65 30 65 65C63 100 35 120 0 122Z" fill="var(--red)"/>
  </svg>
  <svg class="art" style="left:1085px;top:1570px" width="93" height="160" viewBox="0 0 93 160" role="img" aria-label="Illustrated round pepperoni decoration">
    <path d="M93 0V160C40 155 0 120 3 78C6 35 45 3 93 0Z" fill="var(--red)"/>
  </svg>
  <svg class="art" style="left:30px;top:180px" width="40" height="35" viewBox="0 0 40 35" role="img" aria-label="Basil leaf"><ellipse cx="20" cy="17" rx="18" ry="13" fill="var(--basil)"/></svg>
  <svg class="art" style="left:1085px;top:610px" width="50" height="50" viewBox="0 0 50 50" role="img" aria-label="Basil leaf"><ellipse cx="25" cy="25" rx="22" ry="18" fill="var(--basil)"/></svg>

  <div class="masthead-title">Takeout</div>
  <div class="masthead-tag">Locally owned</div>
  <div class="masthead-sub">only</div>

  <div class="rule" style="left:230px;top:433px;width:492px"></div>
  <div class="section-title" style="left:260px;top:445px">RED PIZZAS</div>
  <div class="section-note" style="left:528px;top:455px">all pizzas are 14"</div>
  <div class="rule" style="left:230px;top:488px;width:492px"></div>

  <div class="rule" style="left:777px;top:433px;width:305px"></div>
  <div class="section-title" style="left:777px;top:445px">WHITE PIZZAS</div>
  <div class="rule" style="left:777px;top:488px;width:305px"></div>

  <div class="vdash" style="left:750px;top:435px;height:1457px"></div>

  <div class="item" style="left:87px;top:506px"><h3>Mozzarella</h3><p>crushed tomato sauce, shredded whole milk mozzarella, grated parmesan and pecorino cheeses, garlic infused extra virgin olive oil</p></div>
  <div class="item" style="left:87px;top:626px"><h3>The Vinci</h3><p>shredded whole milk mozzarella, fresh mozzarella, fresh basil, sauce on top, grated parmesan and pecorino, garlic oil. This is similar to a NY-style margherita pizza</p></div>
  <div class="item" style="left:87px;top:765px"><h3>Toscano</h3><p>Bar-style (flat and crispy) pizza with whole-milk mozzarella, pecorino, parmesan, crushed tomato sauce on top, garlic-infused extra virgin oil, and seasoned with oregano and crushed red chili flakes.</p></div>
  <div class="item" style="left:87px;top:897px"><h3>Meatball Combo</h3><p>mozzarella pie base, slices of house-made meatballs, roasted peppers, and sautéed onions</p></div>
  <div class="item" style="left:87px;top:993px"><h3>West Coast Combo</h3><p>Mozzarella pie with sliced local sausage, roasted mushrooms, and black olives</p></div>
  <div class="item" style="left:87px;top:1095px"><h3>Pepperoni Supreme</h3><p>mozzarella pie base with roasted mushrooms, and vinegar peppers</p></div>
  <div class="item" style="left:87px;top:1199px"><h3>Gar-Leek</h3><p>mozzarella pie base, garlic confit, buttery leeks</p></div>

  <div class="item" style="left:436px;top:506px"><h3>Pepperoni</h3><p>mozzarella pie base, pepperoni cups</p></div>
  <div class="item" style="left:436px;top:593px"><h3>Margherita</h3><p>crushed tomato sauce, fresh mozzarella, fresh basil, parmesan, pecorino, garlic oil</p></div>
  <div class="item" style="left:436px;top:695px"><h3>Sausage Combo</h3><p>mozzarella pie base, cup &amp; char sausage, roasted peppers, sautèed onions</p></div>
  <div class="item" style="left:436px;top:796px"><h3>Soupy Combo</h3><p>mozzarella pie base, local soppressata, roasted peppers, sautèed onions</p></div>
  <div class="item" style="left:436px;top:896px"><h3>El Jefe</h3><p>Mozzarella pizza with cup and char sausage, roasted onions, and banana peppers</p></div>
  <div class="item" style="left:436px;top:995px"><h3>Hawaiian</h3><p>pepperoni pie base, roasted green hatch chiles (medium spice level), fresh cut pineapple</p></div>
  <div class="item" style="left:436px;top:1110px;width:300px"><h3>Towner</h3><p>Start with a Toscano pie, then add roasted tomatoes, buttery leeks, and house-made meatball</p></div>

  <div class="item" style="left:781px;top:506px;width:320px"><h3>White</h3><p>shredded mozzarella, fresh mozzarella, pecorino, parmesan, ricotta, fresh basil, garlic oil (no sauce)</p></div>
  <div class="item" style="left:781px;top:600px;width:280px"><h3>Spinach B.L.T.</h3><p>spinach pie base, buttery leeks, bacon, roasted tomato</p></div>
  <div class="item" style="left:781px;top:690px;width:300px"><h3>Potato Pie</h3><p>sliced russets, buttery leeks, fresh mozzarella, medium cheddar, bacon, parmesan, pecorino, garlic oil (no sauce)</p></div>
  <div class="item" style="left:781px;top:804px;width:320px"><h3>Apple Pie</h3><p>medium cheddar, parmesan, pecorino, tart apples, bacon, fresh mozzarella, sautèed onions, garlic oil, and comes with a side of hot honey to drizzle</p></div>
  <div class="item" style="left:781px;top:918px;width:300px"><h3>Spinach</h3><p>white pie base, baby spinach, garlic confit</p></div>
  <div class="item" style="left:781px;top:1006px;width:300px"><h3>Veggie</h3><p>white pie base with fresh spinach, roasted mushrooms, roasted peppers, sautèed onions, roasted tomatoes</p></div>
  <div class="item" style="left:781px;top:1120px;width:310px"><h3>Chicken Bacon Ranch</h3><p>shredded mozzarella, cheddar, roasted chicken, bacon, leeks, roasted tomatoes, ranch drizzle</p></div>

  <div class="dash" style="left:87px;top:1273px;width:650px"></div>
  <div class="dash" style="left:750px;top:1273px;width:220px"></div>

  <div class="rule" style="left:87px;top:1308px;width:635px"></div>
  <div class="section-title" style="left:87px;top:1320px">CUSTOM PIZZA</div>
  <div class="section-note" style="left:433px;top:1325px">Start with either our red or white pie and add what you'd like!<br>Build your own whole pie or half/half!</div>
  <div class="rule" style="left:87px;top:1363px;width:635px"></div>

  <div class="rule" style="left:781px;top:1308px;width:246px"></div>
  <div class="section-title" style="left:781px;top:1320px;width:301px;text-align:center">SIDES</div>
  <div class="rule" style="left:781px;top:1363px;width:301px"></div>

  <div class="item" style="left:87px;top:1389px"><h3>BYOP Mozzarella</h3><p>starts with crushed tomato sauce, shredded mozzarella, parmesan, pecorino, garlic oil</p></div>
  <div class="item" style="left:435px;top:1389px"><h3>BYOP White</h3><p>starts with shredded mozzarella, fresh mozzarella, pecorino, parmesan, ricotta, fresh basil, garlic oil (no sauce)</p></div>

  <div class="rule" style="left:87px;top:1507px;width:635px"></div>
  <div class="section-title" style="left:87px;top:1518px;width:635px;text-align:center">GREENS</div>
  <div class="rule" style="left:87px;top:1562px;width:635px"></div>

  <div class="item" style="left:87px;top:1580px"><h3>Caesar Salad</h3><p>With house-made sourdough croutons, shaved parmesan, lemon wedge, and 2 house-made Caesar dressings</p></div>
  <div class="item" style="left:436px;top:1580px;width:300px"><h3>Chop Salad</h3><p>Mixed greens, diced chicken, bacon, gorgonzola, ditalini pasta, red onion, roasted tomatoes, with 2 sides of house-made balsamic vinaigrette</p></div>

  <div class="dash" style="left:87px;top:1690px;width:650px"></div>

  <div class="item" style="left:781px;top:1389px"><h3>Fries</h3><p style="margin-top:2px">house-cut!</p></div>
  <div class="item" style="left:781px;top:1458px;width:330px"><h3>Garlic Focaccia Bread</h3><p>A lightly stretched dough, shredded whole milk mozzarella, pecorino and parmesan cheeses, and lots of garlic infused extra virgin olive oil. comes with a side of house-made marinara</p></div>
  <div class="item" style="left:781px;top:1590px"><h3>Fruit Sodas</h3><p>Choose a flavor</p></div>
  <div class="item" style="left:781px;top:1675px;width:270px"><h3>Wings</h3><p>6 crispy wingdings tossed in your choice of sauce, or plain</p></div>
  <div class="item" style="left:781px;top:1776px"><h3>Chicken Nuggets</h3><p>For the kids! 10 piece</p></div>
  <div class="item" style="left:781px;top:1855px"><h3>Soda</h3><p>12oz can. Choose a flavor</p></div>

  <div class="order-head">ORDER ONLINE</div>
  <svg class="icon" style="left:92px;top:1786px" width="58" height="58" viewBox="0 0 24 24" aria-hidden="true">
    <path fill="var(--red)" d="M6.6 10.8a15.1 15.1 0 0 0 6.6 6.6l2.2-2.2c.3-.3.7-.4 1-.2 1.1.4 2.3.6 3.6.6.6 0 1 .4 1 1V20c0 .6-.4 1-1 1A17 17 0 0 1 3 4c0-.6.4-1 1-1h3.5c.6 0 1 .4 1 1 0 1.3.2 2.5.6 3.6.1.3 0 .7-.2 1z"/>
  </svg>
  <div class="order-phone">401.555.0142</div>
  <svg class="icon" style="left:93px;top:1858px" width="30" height="38" viewBox="0 0 24 30" aria-hidden="true">
    <path fill="var(--red)" d="M12 0A11 11 0 0 0 1 11c0 8 11 19 11 19s11-11 11-19A11 11 0 0 0 12 0zm0 15a4 4 0 1 1 0-8 4 4 0 0 1 0 8z"/>
  </svg>
  <div class="order-address">17 HARBOR LANE WESTERLY, RI 02891</div>

  <svg class="allergy-band" viewBox="0 0 1178 100" preserveAspectRatio="none" aria-hidden="true">
    <path d="M0 14C40 6 70 18 110 10S190 4 230 12 310 20 350 8 430 2 470 12 560 18 600 8 690 4 730 14 810 18 850 8 930 4 980 14 1060 18 1100 8 1178 10 1178 10V100H0Z" fill="var(--red)"/>
  </svg>
  <div class="allergy-note">Please note: please inform us of any food allergies prior to ordering</div>
</main>
</body>
</html>
```